Creative & Appealing Business Card

Required a business card for Ferndale Recoveries
We specialise in claims management services for PPI ( Payment Protection Insurance.
2 sided business card
Round Corners
I like embossed and raised lettering

Industry/Entity Type

Business

```html
<!DOCTYPE html>
<html lang="en">
<head>
<meta charset="utf-8">
<title>Ferndale Recoveries – Business Card</title>
<link rel="stylesheet" href="https://fonts.googleapis.com/css2?family=Arimo:wght@400;700&display=swap">
<style>
  :root {
    --page: #ffffff;
    --front-light: #e3f4f5;
    --front-deep: #c3eff5;
    --back-bg: #eeefef;
    --ink: #3f5e69;
    --ink-name: #4b6c78;
    --brand-ink: #5f7f89;
    --emboss: #f1f5f5;
    --rule: #7f9498;
    --icon: #2f3f45;
    --back-accent: #a6b1b4;
  }
  * { box-sizing: border-box; margin: 0; padding: 0; }
  html, body {
    width: 1067px;
    height: 1200px;
    overflow: hidden;
    background: var(--page);
    font-family: "Arimo", Arial, sans-serif;
  }
  .canvas { position: relative; width: 1067px; height: 1200px; }

  .card {
    position: absolute;
    border-radius: 24px;
    overflow: hidden;
  }
  .card--front {
    left: 70px; top: 38px; width: 938px; height: 533px;
    background: linear-gradient(135deg, var(--front-light) 0%, var(--front-light) 45%, var(--front-deep) 100%);
  }
  .card--back {
    left: 62px; top: 624px; width: 954px; height: 544px;
    background: var(--back-bg);
  }

  .brand-mark {
    position: absolute;
    left: 73px; top: 61px;
    width: 196px; height: 196px;
    border-radius: 50%;
    background: var(--emboss);
  }
  .brand-name {
    position: absolute;
    left: 306px; top: 122px;
    font-size: 56px;
    font-weight: 700;
    letter-spacing: -0.5px;
    color: var(--brand-ink);
    white-space: nowrap;
  }
  .divider {
    position: absolute;
    left: 306px; top: 252px;
    width: 550px;
    border-top: 2px dotted var(--rule);
  }
  .services {
    position: absolute;
    left: 306px; top: 318px;
    color: var(--ink);
  }
  .services__title {
    font-size: 29px;
    font-weight: 700;
    line-height: 33px;
  }
  .services__subtitle {
    font-size: 29px;
    line-height: 33px;
  }
  .services__list {
    list-style: none;
    margin-top: 22px;
    font-size: 25px;
    line-height: 34px;
  }
  .services__list li::before { content: "• "; }

  .back-accent {
    position: absolute;
    left: -310px; top: -40px;
    width: 630px; height: 630px;
    border-radius: 50%;
    background: var(--back-accent);
  }

  .contact {
    position: absolute;
    left: 472px; top: 100px;
    color: var(--ink-name);
  }
  .contact__name {
    font-size: 30px;
    font-weight: 700;
    margin-left: 35px;
  }
  .contact__group { margin-top: 36px; }
  .contact__group + .contact__group { margin-top: 34px; }
  .contact__row {
    display: flex;
    align-items: center;
    font-size: 27px;
    line-height: 34px;
    white-space: nowrap;
  }
  .contact__row--indent { padding-left: 35px; }
  .contact__icon {
    width: 22px; height: 22px;
    margin-right: 13px;
    fill: var(--icon);
    flex: none;
  }
</style>
</head>
<body>
<main class="canvas">

  <section class="card card--front" aria-label="Card front">
    <div class="brand-mark" aria-hidden="true"></div>
    <div class="brand-name">Ferndale Recoveries</div>
    <div class="divider"></div>
    <div class="services">
      <p class="services__title">CLAIMS MANAGEMENT</p>
      <p class="services__subtitle">SERVICE FOR MIS-SOLD:</p>
      <ul class="services__list">
        <li>Payment Protection Insurance Claims</li>
        <li>Interest Rate Hedging Products/SWAPS</li>
      </ul>
    </div>
  </section>

  <section class="card card--back" aria-label="Card back">
    <div class="back-accent" aria-hidden="true"></div>
    <div class="contact">
      <p class="contact__name">Mara Ellison</p>

      <div class="contact__group">
        <p class="contact__row">
          <svg class="contact__icon" viewBox="0 0 24 24" aria-hidden="true"><path d="M6.6 10.8c1.4 2.8 3.8 5.1 6.6 6.6l2.2-2.2c.3-.3.7-.4 1-.2 1.1.4 2.3.6 3.6.6.6 0 1 .4 1 1V20c0 .6-.4 1-1 1C10.6 21 3 13.4 3 4c0-.6.4-1 1-1h3.5c.6 0 1 .4 1 1 0 1.3.2 2.5.6 3.6.1.3 0 .7-.2 1L6.6 10.8z"/></svg>
          +44 (0) 300 555 0148
        </p>
        <p class="contact__row">
          <svg class="contact__icon" viewBox="0 0 24 24" aria-hidden="true"><rect x="3" y="3" width="5" height="18" rx="1"/><path d="M9 7h12v14H9z"/><rect x="11" y="3" width="8" height="3"/><rect x="11" y="9" width="8" height="3" fill="#eeefef"/><rect x="11" y="14" width="2" height="2" fill="#eeefef"/><rect x="15" y="14" width="2" height="2" fill="#eeefef"/><rect x="11" y="17" width="2" height="2" fill="#eeefef"/><rect x="15" y="17" width="2" height="2" fill="#eeefef"/></svg>
          +44 (0) 208 555 0163
        </p>
      </div>

      <div class="contact__group">
        <p class="contact__row">
          <svg class="contact__icon" viewBox="0 0 24 24" aria-hidden="true"><path d="M12 2a7 7 0 0 0-7 7c0 5.2 7 13 7 13s7-7.8 7-13a7 7 0 0 0-7-7zm0 9.5A2.5 2.5 0 1 1 12 6.5a2.5 2.5 0 0 1 0 5z"/></svg>
          42 Alder Grove Road
        </p>
        <p class="contact__row contact__row--indent">London, NW6 2QT</p>
      </div>

      <div class="contact__group">
        <p class="contact__row">
          <svg class="contact__icon" viewBox="0 0 24 24" aria-hidden="true"><path d="M3 6h18v12H3z"/><path d="M3 6l9 7 9-7" fill="none" stroke="#eeefef" stroke-width="1.8"/></svg>
          mara@ferndalerecoveries.com
        </p>
        <p class="contact__row">
          <svg class="contact__icon" viewBox="0 0 24 24" aria-hidden="true"><circle cx="12" cy="12" r="9" fill="none" stroke="#2f3f45" stroke-width="2"/><ellipse cx="12" cy="12" rx="4" ry="9" fill="none" stroke="#2f3f45" stroke-width="1.6"/><path d="M3 12h18M5 7.5h14M5 16.5h14" stroke="#2f3f45" stroke-width="1.6"/></svg>
          www.ferndalerecoveries.com
        </p>
      </div>
    </div>
  </section>

</main>
</body>
</html>
```